Healthcare technology company needs website design

We need a logo for a new company based in the U.S. We develop software to assist consumers identifying lowest cost healthcare coverage methods, including insurance, discount cards, and cash options. We would like to see designs that use multiple shades of green with the optional addition of other complimentary colors. The final design should communicate a unique blend of saving money while receiving the healthcare you need.
Need the following pages/sections: Homepage, Solutions, About Us, Contact
Competitors: www.velorimed.example; www.qzplo.example

Target Market(s)

Businesses

Industry/Entity Type

Healthcare

Coding

Coded - Design and coding required

Number of Pages Required

4 page

Colors
0054AA
0677BA
7BADD7
CADEEF
E8F1F8
00AB8E
00BBA5
67D7C9
C6EFE9
E9F9F6

Requirements
Must have
• Matching color theme with logo
Nice to have
• Animated background

```html
<!DOCTYPE html>
<html lang="en">
<head>
<meta charset="utf-8">
<title>Fernway Health – Healthcare Technology</title>
<link href="https://fonts.googleapis.com/css2?family=Montserrat:wght@400;500;600;700;800&family=Open+Sans:wght@400;600&display=swap" rel="stylesheet">
<style>
:root{
  --green:#1f7a2e;
  --green-dark:#17621f;
  --green-soft:#e6f2e7;
  --blue:#1b7fd1;
  --blue-deep:#0054aa;
  --ink:#222;
  --muted:#666;
  --footer:#23272f;
  --white:#fff;
}
*{box-sizing:border-box;margin:0;padding:0}
html,body{width:1200px;height:3608px;overflow:hidden}
body{font-family:"Open Sans",Arial,sans-serif;color:var(--ink);background:var(--white);position:relative}
h1,h2,h3,h4,.nav,.btn,.eyebrow{font-family:"Montserrat",Arial,sans-serif}

/* header */
.site-header{position:absolute;top:0;left:0;width:1200px;height:100px;border-bottom:4px solid var(--green);display:flex;align-items:center;justify-content:space-between;padding:0 60px;background:var(--white)}
.brand{display:flex;align-items:center;gap:10px;font-family:"Montserrat",sans-serif;font-weight:700;font-size:22px;color:var(--green)}
.brand-dot{width:30px;height:30px;border-radius:50%;background:var(--green)}
.nav{display:flex;align-items:center;gap:14px;font-size:13px;font-weight:600;color:var(--ink)}
.nav a{color:inherit;text-decoration:none;padding:8px 18px;border-radius:20px}
.nav a.active{border:2px solid var(--green);color:var(--green)}
.social{display:flex;gap:8px;margin-left:16px}
.social span{width:22px;height:22px;border-radius:50%;background:var(--blue)}

/* hero */
.hero{position:absolute;top:104px;left:0;width:1200px;height:608px;background:linear-gradient(120deg,#3d4a52 0%,#222b30 45%,#1a3a48 70%,#2a2f33 100%)}
.hero-text{position:absolute;left:92px;top:200px;color:var(--white)}
.hero-text .light{font-family:"Montserrat",sans-serif;font-weight:400;font-size:66px;line-height:1}
.hero-text h1{font-weight:800;font-size:72px;letter-spacing:1px;line-height:1.2}
.hero-text p{font-family:"Montserrat",sans-serif;font-weight:600;font-size:24px;margin-top:14px}

/* solutions */
.solutions-band{position:absolute;top:712px;left:0;width:1200px;height:368px;background:var(--green)}
.section-head{position:absolute;left:0;width:1200px;text-align:center}
.eyebrow{font-size:18px;font-weight:600}
.section-head h2{font-size:46px;font-weight:800;letter-spacing:1px;margin-top:2px}
.solutions-head{top:776px;color:var(--white)}
.card{position:absolute;top:904px;width:330px;height:284px;background:var(--white);border-radius:6px;box-shadow:0 6px 22px rgba(0,0,0,.12);text-align:center;padding-top:30px}
.icon-circle{width:110px;height:110px;border-radius:50%;background:var(--blue);margin:0 auto;display:flex;align-items:center;justify-content:center}
.card h3{font-size:24px;font-weight:500;margin-top:24px}
.card p{font-size:14px;color:var(--muted);margin:14px auto 0;width:230px;line-height:1.5}

/* about */
.about-photo{position:absolute;left:76px;top:1324px;width:396px;height:376px;border-radius:18px;border:4px solid var(--green);background:linear-gradient(135deg,#4c4f52,#2a2c2f 60%,#5b5e61)}
.about-copy{position:absolute;left:552px;top:1340px;width:560px}
.about-copy .eyebrow{color:var(--green);font-size:18px}
.about-copy h2{font-family:"Montserrat",sans-serif;font-weight:800;font-size:48px;color:var(--green);letter-spacing:1px;margin-top:2px}
.about-copy p{font-size:15px;color:var(--muted);line-height:1.7;margin-top:18px}
.btn{display:inline-block;margin-top:44px;border:2px solid var(--green);color:var(--green);border-radius:24px;font-size:13px;font-weight:700;padding:12px 30px}

/* testimonials */
.testimonials{position:absolute;top:1852px;left:0;width:1200px;height:600px;background:linear-gradient(120deg,rgba(27,127,209,.95),rgba(0,84,170,.9)),linear-gradient(90deg,#6a8aa0,#2c4860);color:var(--white);text-align:center}
.testimonials h2{font-size:48px;font-weight:800;margin-top:100px;letter-spacing:1px}
.quote-badge{width:84px;height:84px;border-radius:50%;background:var(--white);margin:40px auto 0;display:flex;align-items:center;justify-content:center;font-family:Georgia,serif;font-size:60px;color:var(--blue);line-height:1;padding-top:24px}
.testimonials blockquote{width:760px;margin:40px auto 0;font-size:17px;line-height:1.75}
.testimonials cite{display:block;margin-top:44px;font-style:normal;font-family:"Montserrat",sans-serif;font-weight:600;font-size:20px}
.testimonials cite span{font-weight:400;font-size:15px}
.arrow{position:absolute;top:280px}

/* blogs */
.blogs-head{top:2592px;color:var(--blue)}
.blogs-head .eyebrow{font-size:18px}
.blogs-head h2{font-size:42px;color:var(--blue)}
.post{position:absolute;top:2708px;width:336px;height:396px;border:4px solid var(--green);border-radius:14px;overflow:hidden;background:var(--white);box-shadow:0 6px 20px rgba(0,0,0,.1)}
.post-media{height:232px}
.post-body{padding:22px 24px}
.post h4{font-size:17px;font-weight:600}
.post .meta{display:flex;gap:20px;font-size:11px;color:var(--muted);margin-top:8px}
.post .meta i{display:inline-block;width:10px;height:10px;border:1.5px solid var(--green);border-radius:50%;margin-right:5px;vertical-align:-1px}
.post p{font-size:13px;color:var(--muted);line-height:1.6;margin-top:18px}
.post.featured{background:var(--green)}
.post.featured .post-body,.post.featured .meta,.post.featured p{color:var(--white)}
.post.featured .meta i{border-color:var(--white)}

/* footer */
.site-footer{position:absolute;top:3220px;left:0;width:1200px;height:388px;background:var(--footer);color:#cfd3da;font-size:13px}
.footer-brand{position:absolute;left:100px;top:76px;text-align:center;width:160px}
.footer-brand .brand{justify-content:center;color:var(--green);font-size:20px;flex-direction:column;gap:8px}
.footer-social{display:flex;gap:6px;justify-content:center;margin-top:20px}
.footer-social span{width:24px;height:24px;border-radius:50%;background:var(--blue)}
.footer-social span.red{background:#d33}
.footer-brand small{display:block;margin-top:16px;font-size:11px}
.footer-col{position:absolute;top:84px}
.footer-col h4{font-size:17px;font-weight:600;color:var(--white);margin-bottom:22px}
.footer-col ul{list-style:none}
.footer-col li{margin-bottom:12px;font-size:12px;display:flex;align-items:center;gap:10px}
.footer-col li::before{content:"";flex:none;width:8px;height:8px;border-radius:50%;border:1.5px solid var(--green)}
.contact-list li::before{width:14px;height:14px;background:var(--green);border:none}
.news p{width:250px;line-height:1.6;font-size:12px}
.news .field{margin-top:24px;width:240px;height:36px;border-radius:18px;background:var(--white);color:#999;font-size:11px;padding:11px 16px}
.news .subscribe{margin-top:10px;width:240px;height:38px;border-radius:19px;background:var(--blue);color:var(--white);font-family:"Montserrat",sans-serif;font-weight:700;font-size:13px;text-align:center;line-height:38px}
</style>
</head>
<body>

<header class="site-header">
  <div class="brand"><span class="brand-dot"></span>Fernway Health</div>
  <nav class="nav">
    <a class="active">HOME</a><a>ABOUT US</a><a>SOLUTIONS</a><a>CONTACT</a>
    <div class="social"><span></span><span></span></div>
  </nav>
</header>

<section class="hero" role="img" aria-label="Doctor holding a stethoscope behind the back">
  <div class="hero-text">
    <div class="light">Healthcare</div>
    <h1>TECHNOLOGY</h1>
    <p>Low Cost Healthcare Coverage Methods</p>
  </div>
</section>

<div class="solutions-band"></div>
<div class="section-head solutions-head">
  <div class="eyebrow">Medically Recognized Offers</div>
  <h2>OUR SOLUTIONS</h2>
</div>

<article class="card" style="left:80px">
  <div class="icon-circle">
    <svg width="56" height="56" viewBox="0 0 56 56" fill="none" stroke="#fff" stroke-width="3" stroke-linejoin="round"><path d="M28 30 C18 22 16 14 22 11 C25 10 27 12 28 14 C29 12 31 10 34 11 C40 14 38 22 28 30Z" fill="#fff"/><path d="M6 38 L16 34 L30 38 L42 34 C46 33 48 37 44 39 L30 46 L16 44 L6 46"/></svg>
  </div>
  <h3>Insurance</h3>
  <p>Compare plan prices side by side with ease.</p>
</article>
<article class="card" style="left:432px">
  <div class="icon-circle">
    <svg width="58" height="58" viewBox="0 0 58 58" fill="none" stroke="#fff" stroke-width="3" stroke-linejoin="round"><rect x="16" y="10" width="30" height="20" rx="3" fill="#fff"/><path d="M6 40 L16 36 L30 40 L42 36 C46 35 48 39 44 41 L30 48 L16 46 L6 48"/></svg>
  </div>
  <h3>Discount Cards</h3>
  <p>Find savings cards that cut your drug costs.</p>
</article>
<article class="card" style="left:780px">
  <div class="icon-circle">
    <svg width="60" height="60" viewBox="0 0 60 60" fill="none" stroke="#fff" stroke-width="3"><rect x="8" y="16" width="44" height="28" rx="3"/><circle cx="30" cy="30" r="7" fill="#fff"/><path d="M14 22v16M46 22v16"/></svg>
  </div>
  <h3>Cash Options</h3>
  <p>See fair cash prices before every visit today.</p>
</article>

<div class="about-photo" role="img" aria-label="Portrait of a doctor in dark scrubs with folded arms"></div>
<section class="about-copy">
  <div class="eyebrow">Who We Are</div>
  <h2>ABOUT THE FIRM</h2>
  <p>We build simple tools that help people find the lowest cost path to the care they need. Our team blends health know-how with clear data so every choice is easy to make and easy to trust.</p>
  <p>From first search to final bill, we stay beside you and show the savings in plain words.</p>
  <span class="btn">VIEW DETAILS</span>
</section>

<section class="testimonials" role="img" aria-label="Blue tinted photo of a medical team in a bright clinic">
  <h2>TESTIMONIALS</h2>
  <div class="quote-badge">“</div>
  <blockquote>This tool showed us three ways to pay for care and the cheapest one saved our family hundreds. Setup took minutes and the team answered every question we had along the way. We now check prices before every visit and never look back.</blockquote>
  <cite>R. Calloway <span>- Patient</span></cite>
  <svg class="arrow" style="left:120px" width="20" height="30" viewBox="0 0 20 30" fill="none" stroke="#fff" stroke-width="3"><path d="M15 4 L5 15 L15 26"/></svg>
  <svg class="arrow" style="left:1060px" width="20" height="30" viewBox="0 0 20 30" fill="none" stroke="#fff" stroke-width="3"><path d="M5 4 L15 15 L5 26"/></svg>
</section>

<div class="section-head blogs-head">
  <div class="eyebrow">Latest From Blogs</div>
  <h2>OFFERS OF HELP</h2>
</div>

<article class="post" style="left:80px">
  <div class="post-media" role="img" aria-label="Doctor with stethoscope examining a patient" style="background:linear-gradient(135deg,#e9e4df,#c9bfb6)"></div>
  <div class="post-body">
    <h4>Daily Structure - Work</h4>
    <div class="meta"><span><i></i>2 Comments</span><span><i></i>By Admin</span></div>
    <p>Simple steps to lower what you pay for care.</p>
  </div>
</article>
<article class="post featured" style="left:432px">
  <div class="post-media" role="img" aria-label="Dental treatment room with chair and lamp" style="background:linear-gradient(135deg,#dfe6ea,#9fb0ba)"></div>
  <div class="post-body">
    <h4>Administrative Support</h4>
    <div class="meta"><span><i></i>2 Comments</span><span><i></i>By Admin</span></div>
    <p>Simple steps to lower what you pay for care.</p>
  </div>
</article>
<article class="post" style="left:784px">
  <div class="post-media" role="img" aria-label="Group of doctors talking in a hospital hallway" style="background:linear-gradient(135deg,#5a6f86,#c7d3de)"></div>
  <div class="post-body">
    <h4>Daily Structure - Work</h4>
    <div class="meta"><span><i></i>2 Comments</span><span><i></i>By Admin</span></div>
    <p>Simple steps to lower what you pay for care.</p>
  </div>
</article>

<footer class="site-footer">
  <div class="footer-brand">
    <div class="brand"><span class="brand-dot" style="width:44px;height:44px"></span>Fernway Health</div>
    <div class="footer-social"><span></span><span></span><span class="red"></span><span></span></div>
    <small>© 2024 Fernway Health</small>
  </div>
  <div class="footer-col" style="left:360px">
    <h4>Quick Links</h4>
    <ul><li>HOME</li><li>ABOUT US</li><li>SOLUTIONS</li><li>CONTACT</li><li>OFFERS OF HELP</li></ul>
  </div>
  <div class="footer-col" style="left:576px">
    <h4>Contact Details</h4>
    <ul class="contact-list"><li>210 Maple Court, Suite 4,<br>Austin, TX 73301</li><li>(555) 014-2210</li><li>hello@fernway.example</li></ul>
  </div>
  <div class="footer-col news" style="left:856px">
    <h4>Signup For Newsletter</h4>
    <p>Get new ways to save on care sent to your inbox.</p>
    <div class="field">Email address</div>
    <div class="subscribe">SUBSCRIBE</div>
  </div>
</footer>

</body>
</html>
```